Website Design for NYC Female Attorney – Clean, Warm, Professional

Marian Thorpe, Esq.
www.MarianJThorpeLegal.example

I’m a New York City-based attorney and CPA with a reputation for providing thoughtful, high-integrity legal guidance in both estate planning and small business law. I’ve served over 500 clients, and maintain a perfect 5-star rating. Clients come to me for clarity, compassion, and results — and I want my new website to reflect that.

**🎯 WHAT I NEED:**
A clean, modern, and emotionally resonant website that highlights who I am, what I do, and why clients trust me. It must feel approachable and warm, but still professional and elegant — think Quillo meets boutique law firm. Feminine but not frilly.

**🧩 CORE WEBSITE SECTIONS (Top Navigation):**

1. **Home** – Strong first impression, tagline, CTA (book a call)
Homepage Copy (Sample Layout)
Headline:
Trusted Legal Guidance for Families and Founders.

Subheading:
Whether you’re protecting what you’ve built or building what’s next, I help you navigate estate planning and business law with confidence, compassion, and clarity.

Tagline (beneath logo or footer):
Legal Clarity for Life and Business.
2. **About Marian** – Bio, personal approach, credentials
3. **Services**

* *Estate Planning*
* *Business Law*
4. **Who I Work With** – Ideal clients (parents, entrepreneurs, etc.)
5. **Testimonials** – Client praise and social proof
6. **Success Stories** – Highlighting wins and case types
7. **FAQs** – Warm and clear answers to common questions
8. **Blog** – Thought leadership and helpful tips
8.5 Events
9. **Contact / Book a Call** – Scheduling or contact form

**🖼 STYLE DIRECTION:**

* Clean white backgrounds, soft jewel tones or neutrals
* Professional headshots and personal branding assets available
* Emphasis on readability, trust, and ease of navigation - THIS NEEDS TO BE BUILT OUT SO IT IS TRUSTED BY AI!
* No harsh colors, no corporate/legal clichés (e.g., gavels or scales) - I MEAN THIS. I DO NOT WANT A BORING LAW WEBSITE WITH SCALES AND GAVELS
* Feminine edge (not pink-heavy), with strong hierarchy and callouts

**💡 DESIGN NOTES:**

* Mobile-first design required
* Should include space for video or welcome message
* Easy to update blog or CMS area preferred
* Built in a user-friendly platform like WordPress, Webflow, or similar
* Needs to feel elevated enough to support high-end flat fee packages

**📣 TONE:**
Smart. Warm. Sophisticated. Human.

**⚖️ FINAL DELIVERABLES:**

* Homepage + 5+ interior pages
* Desktop + mobile views
* Style guide (fonts, colors, buttons)
* Bonus if you can help with copy layout/structure (not just visuals)

**📍TARGET AUDIENCE:**

* Busy professionals and families in NYC
* Women and couples who want peace of mind
* Entrepreneurs and creatives needing solid legal support

Here is my current site: www.MarianJThorpeLegal.example
And here is a second business I have: www.QuickCounselDaily.example

Families and business owners

Law

Serif
Sans Serif
Script

• This website must be built to be seen as trustworthy by AI.

```html
<!DOCTYPE html>
<html lang="en">
<head>
<meta charset="utf-8">
<title>Law Office of Marian Thorpe</title>
<link rel="stylesheet" href="https://fonts.googleapis.com/css2?family=Krona+One&family=Inter:wght@400;500;600;700&family=Cormorant+Garamond:wght@500;600&display=swap">
<style>
:root{
  --pink:#ec4f89;
  --pink-soft:#f4a3c2;
  --plum:#7a1f4b;
  --plum-dark:#4f1230;
  --blush:#fdf5f8;
  --band:#fbe6ef;
  --ink:#1f1a1d;
  --muted:#7b7278;
  --line:#f1d5e0;
  --white:#ffffff;
}
*{box-sizing:border-box;margin:0;padding:0}
html,body{width:1200px;height:5223px;overflow:hidden}
body{position:relative;background:var(--blush);font-family:"Inter",sans-serif;color:var(--ink)}
.abs{position:absolute}
.display{font-family:"Krona One",sans-serif;text-transform:uppercase;letter-spacing:1px}
.btn{position:absolute;display:flex;align-items:center;justify-content:center;background:var(--pink);color:var(--white);font-size:10px;font-weight:600;border-radius:2px}
.btn-ghost{position:absolute;display:flex;align-items:center;justify-content:center;border:1px solid var(--pink);border-left:3px solid var(--pink);color:var(--pink);font-size:10px;font-weight:500;background:var(--white)}
.photo{position:absolute;border-radius:6px}
.section-title{position:absolute;left:0;width:1200px;display:flex;align-items:center;justify-content:center;gap:26px;font-family:"Krona One",sans-serif;font-size:24px;text-transform:uppercase;letter-spacing:1px}
.section-title::before,.section-title::after{content:"";width:130px;height:1px;background:var(--pink-soft)}
.small{font-size:9px;line-height:15px;color:var(--muted)}

/* header */
.social{position:absolute;top:27px;width:12px;height:12px;border-radius:50%;background:var(--ink)}
.logo-top{position:absolute;left:500px;top:10px;width:200px;text-align:center;font-family:"Cormorant Garamond",serif;color:var(--plum)}
.logo-top .pre{font-size:9px;letter-spacing:4px}
.logo-top .name{font-size:15px;letter-spacing:2px}

/* hero */
.hero{position:absolute;left:24px;top:67px;width:1152px;height:452px;border-radius:36px;background:linear-gradient(135deg,#c23a78 0%,#a42d66 45%,#7c2050 100%)}
.hero-nav{position:absolute;top:24px;left:0;width:100%;display:flex;justify-content:center;gap:0;font-size:11px;font-weight:500;color:var(--white)}
.hero-nav span{padding:0 16px;border-right:1px solid rgba(255,255,255,.35)}
.hero-nav span:last-child{border:none}
.hero-nav .active{text-decoration:underline;text-underline-offset:6px}
.hero h1{position:absolute;top:140px;left:0;width:100%;text-align:center;color:var(--white);font-family:"Krona One",sans-serif;font-size:40px;line-height:53px;font-weight:400}
.hero p{position:absolute;top:246px;left:270px;width:612px;text-align:center;color:var(--white);font-size:11.5px;line-height:18px;font-weight:600}
.hero .cta{position:absolute;left:485px;top:292px;width:182px;height:28px;border:1px solid var(--white);color:var(--white);font-size:10px;display:flex;align-items:center;justify-content:center}
.dots{position:absolute;left:546px;top:418px;display:flex;gap:4px}
.dots i{display:block;width:12px;height:3px;background:rgba(255,255,255,.5)}
.dots i.on{width:22px;background:var(--white)}

/* services */
.svc-card{position:absolute;left:186px;top:1084px;width:826px;height:234px;background:var(--white);border-radius:8px;box-shadow:0 6px 20px rgba(122,31,75,.1)}

/* brand row */
.brand{position:absolute;display:flex;align-items:center;gap:9px;font-size:19px;font-weight:700;color:var(--ink)}
.brand i{display:block;width:30px;height:30px;border-radius:50%;background:var(--ink)}
.sep-dot{position:absolute;width:6px;height:6px;border-radius:50%;background:var(--pink)}

/* testimonials */
.band{position:absolute;left:0;top:1739px;width:1200px;height:440px;background:var(--band)}
.t-card{position:absolute;background:var(--white);border-radius:6px;padding:16px 14px;box-shadow:0 4px 14px rgba(122,31,75,.08)}
.stars{color:#f3a51f;font-size:13px;letter-spacing:3px}
.t-card .small{margin-top:10px;font-size:8.5px;line-height:15px}
.reviewer{display:flex;align-items:center;gap:10px;margin-top:14px;font-size:8px;font-weight:700}
.reviewer i{display:block;width:16px;height:16px;border-radius:50%;background:#e5e1e3}
.reviewer span{display:block;font-weight:400;color:var(--muted)}

/* stories */
.story{position:absolute;background:var(--white);border-radius:6px;padding:18px 18px;box-shadow:0 4px 14px rgba(122,31,75,.09)}
.story h4{font-size:11px;font-weight:600;margin-bottom:18px}
.story .small{font-size:8.5px}
.story .btn-ghost{position:static;width:80px;height:28px;margin-top:12px}

/* faq */
.faq{position:absolute;background:var(--white);border:1px solid var(--line);border-radius:3px;padding:0 14px;font-size:9px;font-weight:600;display:flex;align-items:center;justify-content:space-between}
.faq i{display:block;width:13px;height:13px;border:1px solid var(--muted);border-radius:50%;position:relative}
.faq i::after{content:"+";position:absolute;left:2px;top:-2px;font-style:normal;font-size:10px;color:var(--muted)}
.faq.open{display:block;padding:14px}
.faq.open .q{color:var(--pink);line-height:15px}

/* video */
.video{position:absolute;left:0;top:3256px;width:1200px;height:470px;border-radius:60px 60px 0 0;background:linear-gradient(120deg,#7d2a55 0%,#a64476 55%,#8a3060 100%)}
.play{position:absolute;left:538px;top:158px;width:120px;height:120px;border-radius:50%;border:2px solid rgba(255,255,255,.6)}
.play b{position:absolute;left:40px;top:40px;width:40px;height:40px;border-radius:50%;background:var(--white)}

/* insights */
.insights{position:absolute;left:0;top:3693px;width:1200px;height:1073px;background:var(--blush);border-radius:60px 60px 0 0}
.post{position:absolute;left:235px;width:736px;background:var(--band);border-radius:4px}
.post .img{position:absolute;left:0;top:0;width:187px;height:100%;border-radius:4px 0 0 4px;background:linear-gradient(135deg,#d8d0cf,#8b7b7e)}
.post h3{position:absolute;left:222px;top:20px;width:500px;font-size:18px;font-weight:600;line-height:26px}
.post .meta{position:absolute;left:222px;font-size:7px;color:var(--pink);display:flex;gap:28px}
.post .small{position:absolute;left:222px;width:490px;font-size:8.5px}
.post .small b{color:var(--pink);font-weight:600}

/* events */
.event{position:absolute;top:4378px;height:207px;border-radius:6px;background:linear-gradient(160deg,#d9d3d1,#6f6468)}

/* footer */
.footer{position:absolute;left:0;top:4766px;width:1200px;height:293px;background:linear-gradient(120deg,#c43a77 0%,#95285d 50%,#5c1637 100%)}
.footer .brandmark{position:absolute;left:200px;top:46px;width:260px;text-align:center;color:var(--white);font-family:"Cormorant Garamond",serif}
.footer .brandmark .pre{font-size:16px;letter-spacing:7px}
.footer .brandmark .name{font-size:28px;letter-spacing:4px;margin-top:22px}
.footer .tag{position:absolute;left:200px;top:170px;width:300px;font-size:11px;line-height:20px;color:var(--white)}
.footer h5{position:absolute;font-family:"Krona One",sans-serif;font-size:14px;font-weight:400;color:var(--white)}
.f-line{position:absolute;left:566px;display:flex;gap:10px;font-size:10px;font-weight:600;color:var(--white);line-height:18px}
.field{position:absolute;border:1px solid rgba(255,255,255,.45);font-size:7px;color:rgba(255,255,255,.8);padding:6px 8px}
.backtop{position:absolute;left:580px;top:5074px;width:36px;height:36px;border-radius:50%;background:var(--pink)}
.foot-nav{position:absolute;top:5144px;left:186px;width:826px;display:flex;justify-content:space-between;font-size:9px}
.disclaimer{position:absolute;top:5189px;left:0;width:1200px;text-align:center;font-size:8.5px;color:var(--muted)}
</style>
</head>
<body>

<!-- header -->
<header>
  <span class="social" style="left:193px"></span>
  <span class="social" style="left:222px"></span>
  <span class="social" style="left:252px"></span>
  <div class="logo-top"><div class="pre">LAW OFFICE OF</div><div class="name">MARIAN THORPE</div></div>
  <div class="btn" style="left:898px;top:18px;width:115px;height:31px">Get Started Today</div>
</header>

<!-- hero -->
<section class="hero">
  <nav class="hero-nav">
    <span class="active">Home</span><span>About</span><span>Services</span><span>Estate Planning</span><span>Business Law</span><span>Who I Work With</span><span>Testimonials</span><span>Success Stories</span><span>Contact</span>
  </nav>
  <h1>TRUSTED LEGAL GUIDANCE<br>FOR FAMILIES AND FOUNDERS.</h1>
  <p>Whether you’re protecting what you’ve built or building what’s next, I help you navigate estate planning and business law with confidence, compassion, and clarity.</p>
  <div class="cta">BOOK MEETING WITH MARIAN</div>
  <div class="dots"><i></i><i class="on"></i><i></i></div>
</section>

<!-- about -->
<section>
  <h2 class="section-title" style="top:606px">About Marian</h2>
  <div class="photo" role="img" aria-label="Columned courthouse facade" style="left:186px;top:661px;width:203px;height:227px;background:linear-gradient(160deg,#e9eef3,#8c98a6)"></div>
  <div class="photo" role="img" aria-label="Portrait of Marian seated" style="left:405px;top:707px;width:201px;height:227px;background:linear-gradient(160deg,#c7cfdc,#6f7480)"></div>
  <h3 class="abs" style="left:645px;top:686px;width:370px;font-size:13px;font-weight:500;line-height:20px">Do you want to create a will or living trust, but haven’t gotten around to it?</h3>
  <p class="abs small" style="left:645px;top:740px;width:370px;font-size:8.5px">Our simple and convenient process will give you the peace of mind of knowing you finally have your affairs in order. Getting started is all handled online via e-signature and online payment. We personally guide you through information gathering. No lengthy intake forms. The first draft contains a easy to read summary and personalized explanation video. Final documents are signed and notarized at your home or in our Midtown Manhattan office.</p>
  <p class="abs" style="left:645px;top:865px;font-size:8px;color:var(--pink);font-weight:600">Marian Thorpe, Esq., CPA</p>
  <p class="abs" style="left:645px;top:880px;font-size:8px;color:var(--muted)">Founder and Managing Attorney</p>
  <div class="btn" style="left:645px;top:906px;width:83px;height:28px">Learn More</div>
</section>

<!-- services -->
<section>
  <h2 class="section-title" style="top:1024px">Services Overview</h2>
  <div class="svc-card">
    <h3 class="abs" style="left:19px;top:26px;font-size:18px;font-weight:600">Business Law</h3>
    <div class="abs" style="left:0;top:64px;width:560px;height:1px;background:var(--line)"></div>
    <div class="abs" role="img" aria-label="Business meeting in a glass office" style="left:558px;top:13px;width:249px;height:48px;border-radius:4px;background:linear-gradient(90deg,#3f4650,#1e232a)"></div>
    <h3 class="abs" style="left:19px;top:94px;font-size:18px;font-weight:600">Estate Planning</h3>
    <p class="abs small" style="left:19px;top:127px;width:430px;font-size:8.5px">Our simple and convenient process will give you the peace of mind of knowing you finally have your affairs in order. Getting started is all handled online and easily paid.</p>
    <div class="btn" style="left:19px;top:171px;width:81px;height:28px">Explore All</div>
    <div class="abs" role="img" aria-label="Attorney reviewing documents with a client" style="left:558px;top:82px;width:249px;height:131px;border-radius:4px;background:linear-gradient(135deg,#c9c2b8,#4e4a47)"></div>
  </div>
  <div class="btn-ghost" style="left:547px;top:1342px;width:106px;height:28px">View All Services</div>
</section>

<!-- who i work with -->
<section>
  <h2 class="section-title" style="top:1460px">Who I Work With</h2>
  <div class="brand" style="left:186px;top:1519px"><i></i>Brightleaf</div>
  <div class="brand" style="left:416px;top:1519px"><i></i>Corvane</div>
  <div class="brand" style="left:643px;top:1519px"><i></i>Halden</div>
  <div class="brand" style="left:870px;top:1519px"><i></i>Mirova</div>
  <div class="brand" style="left:186px;top:1611px"><i></i>Talbrook</div>
  <div class="brand" style="left:416px;top:1611px"><i></i>Ostera</div>
  <div class="brand" style="left:643px;top:1611px"><i></i>Veyline</div>
  <div class="brand" style="left:870px;top:1611px"><i></i>Kestrel</div>
  <span class="sep-dot" style="left:368px;top:1574px"></span>
  <span class="sep-dot" style="left:595px;top:1574px"></span>
  <span class="sep-dot" style="left:822px;top:1574px"></span>
</section>

<!-- testimonials -->
<section class="band">
  <h2 class="section-title" style="top:45px;font-size:22px">Trusted by 500+ clients and counting.</h2>
  <div class="t-card" style="left:186px;top:102px;width:262px;height:237px">
    <div class="stars">★★★★☆</div>
    <p class="small">My wife and I used Marian to design and execute our estate plan. She is incredibly organized and efficient with her time. As parents of two young children we valued the time she spent explaining our options and the care she took in preparing our documents. Marian goes above and beyond for her clients. I would certainly recommend her to individuals or families looking to set up a trust.</p>
    <div class="reviewer"><i></i><div>Delia Marsh<span>Client</span></div></div>
  </div>
  <div class="t-card" style="left:468px;top:102px;width:260px;height:204px">
    <div class="stars">★★★★☆</div>
    <p class="small">So happy with Marian and our experience making our estate plans! We had dreaded this for years and she made what could have been a daunting process truly painless. She guided us to the best option for our family and was absolutely transparent as to pricing and services included.</p>
    <div class="reviewer"><i></i><div>Joan Whitaker<span>Client</span></div></div>
  </div>
  <div class="t-card" style="left:750px;top:102px;width:259px;height:190px">
    <div class="stars">★★★★☆</div>
    <p class="small">Our relationship with Marian started with a very informative estate planning information session which clarified many open questions that we had about wills and trusts in an relaxed tour very professional.</p>
    <div class="reviewer"><i></i><div>Peter Alcott<span>Client</span></div></div>
  </div>
  <svg class="abs" style="left:560px;top:351px" width="80" height="36" viewBox="0 0 80 36">
    <circle cx="18" cy="18" r="17" fill="#fff" stroke="#ec4f89"/>
    <path d="M23 18H13M17 14l-4 4 4 4" stroke="#ec4f89" fill="none" stroke-width="1.5"/>
    <circle cx="62" cy="18" r="17" fill="#ec4f89"/>
    <path d="M57 18h10M63 14l4 4-4 4" stroke="#fff" fill="none" stroke-width="1.5"/>
  </svg>
</section>

<!-- success stories -->
<section>
  <h2 class="section-title" style="top:2266px">Successfull Stories</h2>
  <div class="story" style="left:186px;top:2323px;width:232px;height:203px">
    <h4>Failure to transfer shares</h4>
    <p class="small">Our simple and convenient process will give you the peace of mind of knowing you finally have your affairs in order. Getting started is all handled online via e-signature and online payment.</p>
    <div class="btn-ghost">Know More</div>
  </div>
  <div class="story" style="left:186px;top:2552px;width:232px;height:201px">
    <h4>A business data breach</h4>
    <p class="small">Our simple and convenient process will give you the peace of mind of knowing you finally have your affairs in order. Getting started is all handled online via e-signature and online payment.</p>
    <div class="btn-ghost">Know More</div>
  </div>
  <div class="abs" role="img" aria-label="Colleagues reviewing a case file in an office" style="left:436px;top:2323px;width:328px;height:430px;border-radius:8px;background:linear-gradient(180deg,#a36a88 0%,#8a3f66 55%,#6f2750 100%)">
    <h4 class="abs" style="left:18px;top:254px;color:#fff;font-size:11px;font-weight:600">Failure to transfer shares</h4>
    <p class="abs" style="left:18px;top:283px;width:292px;font-size:8.5px;line-height:15px;color:#fff">Our simple and convenient process will give you the peace of mind of knowing you finally have your affairs in order. Getting started is all handled online via e-signature and online payment. We personally guide you through information gathering. No lengthy intake forms.</p>
    <div class="btn" style="left:18px;top:362px;width:82px;height:28px">Know More</div>
  </div>
  <div class="story" style="left:782px;top:2323px;width:230px;height:203px">
    <h4>Breach of Fiduciary Duty Case</h4>
    <p class="small">Our simple and convenient process will give you the peace of mind of knowing you finally have your affairs in order. Getting started is all handled online via e-signature and online payment.</p>
    <div class="btn-ghost">Know More</div>
  </div>
  <div class="story" style="left:782px;top:2552px;width:230px;height:201px">
    <h4>Breach of Contract and Fraud</h4>
    <p class="small">Our simple and convenient process will give you the peace of mind of knowing you finally have your affairs in order. Getting started is all handled online via e-signature and online payment.</p>
    <div class="btn-ghost">Know More</div>
  </div>
</section>

<!-- faq -->
<section>
  <h2 class="section-title" style="top:2840px">Frequently Asked Questions</h2>
  <div class="faq" style="left:186px;top:2899px;width:402px;height:34px">How can I learn more about Marian Thorpe?<i></i></div>
  <div class="faq open" style="left:186px;top:2949px;width:402px;height:112px">
    <div class="q">Can we have a quick call before booking the Peace of Mind Planning Session?</div>
    <p class="small" style="margin-top:8px;font-weight:400;font-size:8px">A person who has to follow section 44AB and does not get his accounts audited or submit the report as per section 44AB for any year or years may face a penalty from the Assessing Officer.</p>
  </div>
  <div class="faq" style="left:186px;top:3075px;width:402px;height:34px">How can I learn more about the Law Office of Marian Thorpe?<i></i></div>
  <div class="faq" style="left:612px;top:2899px;width:400px;height:34px">What is our general process?<i></i></div>
  <div class="faq" style="left:612px;top:2951px;width:400px;height:34px">What are the initial steps to get started?<i></i></div>
  <div class="faq" style="left:612px;top:3004px;width:400px;height:34px">What if I need to update my estate planning documents?<i></i></div>
  <div class="faq" style="left:612px;top:3057px;width:400px;height:34px">Isn’t estate planning just for the wealthy?<i></i></div>
  <div class="btn" style="left:547px;top:3132px;width:104px;height:28px">Explore All FAQ</div>
</section>

<!-- video -->
<section class="video" role="img" aria-label="Welcome video still of an attorney meeting with clients">
  <div class="play"><b></b>
    <svg class="abs" style="left:54px;top:51px" width="14" height="18" viewBox="0 0 14 18"><path d="M1 1l12 8-12 8z" fill="#ec4f89"/></svg>
  </div>
</section>

<!-- insights + events -->
<section class="insights">
  <h2 class="section-title" style="top:88px">Legal Insights &amp; Expert Opinions</h2>
  <article class="post" style="top:144px;height:164px">
    <div class="img" role="img" aria-label="Three attorneys standing together"></div>
    <h3>Data Privacy Regulations: What Businesses Need to Know</h3>
    <div class="meta" style="top:83px"><span>May 3, 2025</span><span>By Ana Reyes</span><span>0 comments</span></div>
    <p class="small" style="top:100px">Our simple and convenient process will give you the peace of mind of knowing you finally have your affairs in order. Getting started is all handled online via e-signature and online payment. We personally guide you through information gathering. No lengthy intake forms. <b>More...</b></p>
  </article>
  <article class="post" style="top:329px;height:156px">
    <div class="img" role="img" aria-label="Team of attorneys in a meeting"></div>
    <h3>Effective Dispute Resolution Techniques for Business Success</h3>
    <div class="meta" style="top:80px"><span>May 3, 2025</span><span>By Ana Reyes</span><span>0 comments</span></div>
    <p class="small" style="top:97px">Our simple and convenient process will give you the peace of mind of knowing you finally have your affairs in order. Getting started is all handled online via e-signature and online payment. We personally guide you through information gathering. No lengthy intake forms. <b>More...</b></p>
  </article>
  <div class="abs" style="left:991px;top:232px;width:3px;height:56px;background:#8a7f85;border-radius:2px"></div>
  <div class="btn-ghost" style="left:547px;top:513px;width:106px;height:28px">Explore All News</div>
  <h2 class="section-title" style="top:629px">Events</h2>
</section>
<div class="event" role="img" aria-label="Colleagues discussing documents" style="left:0;width:213px"></div>
<div class="event" role="img" aria-label="Two professionals in a hallway" style="left:239px;width:223px"></div>
<div class="event" role="img" aria-label="Business team outside an office building" style="left:488px;width:225px;height:294px;background:linear-gradient(180deg,#c8c3c6 0%,#8d6d7e 55%,#7a2f57 100%)">
  <p class="abs" style="left:20px;top:208px;color:#fff;font-size:12px;font-weight:600;line-height:19px">Understanding the New<br>Financial.</p>
  <div class="abs" style="left:20px;top:249px;width:62px;height:26px;border:1px solid #fff;color:#fff;font-size:9px;display:flex;align-items:center;justify-content:center">View All</div>
</div>
<div class="event" role="img" aria-label="Attorneys reviewing files" style="left:736px;width:225px"></div>
<div class="event" role="img" aria-label="Women reading a report in an office" style="left:985px;width:215px"></div>

<!-- footer -->
<footer class="footer">
  <div class="brandmark"><div class="pre">LAW OFFICE OF</div><div class="name">MARIAN THORPE</div></div>
  <p class="tag">We help individuals and families protect their assets and loved ones with proper estate planning.</p>
  <h5 style="left:566px;top:78px">CONTACT US</h5>
  <div class="f-line" style="top:108px"><svg width="10" height="12" viewBox="0 0 10 12"><path d="M2 1l2 0 1 3-1.5 1a6 6 0 0 0 2.5 3l1-1.5 3 1v2c0 1-1 1.5-2 1.3C4 10 1 6 1 2.5 1 1.5 1.3 1 2 1z" fill="#fff"/></svg>(212) 555-0148</div>
  <div class="f-line" style="top:138px"><svg width="11" height="10" viewBox="0 0 11 10"><rect x=".5" y="1" width="10" height="8" rx="1" fill="#fff"/><path d="M1 1.5l4.5 4 4.5-4" stroke="#95285d" fill="none"/></svg>hello@marianthorpelegal.example</div>
  <div class="f-line" style="top:166px"><svg width="10" height="13" viewBox="0 0 10 13"><path d="M5 1a4 4 0 0 1 4 4c0 3-4 7-4 7S1 8 1 5a4 4 0 0 1 4-4z" fill="#fff"/><circle cx="5" cy="5" r="1.5" fill="#95285d"/></svg><span>410 Harlow Ave, Fl 12<br>New York, NY 10001</span></div>
  <h5 style="left:803px;top:76px;font-size:12px">HAVE ANY QUESTIONS?</h5>
  <div class="field" style="left:803px;top:103px;width:101px;height:20px">Enter Your Name</div>
  <div class="field" style="left:910px;top:103px;width:100px;height:20px">Enter Your Name</div>
  <div class="field" style="left:803px;top:135px;width:207px;height:29px">Message</div>
  <div class="btn" style="left:803px;top:180px;width:87px;height:29px">Submit Now</div>
</footer>
<div class="backtop"><svg class="abs" style="left:12px;top:12px" width="12" height="12" viewBox="0 0 12 12"><path d="M6 10V2M2 6l4-4 4 4" stroke="#fff" stroke-width="1.5" fill="none"/></svg></div>
<nav class="foot-nav"><span>Home</span><span>About</span><span>Services</span><span>Estate Planning</span><span>Business Law</span><span>Who I Work With</span><span>Testimonials</span><span>Success Stories</span><span>FAQs</span><span>Blog</span><span>Events</span><span>Contact</span></nav>
<p class="disclaimer">Disclaimer: The Information You Obtain At This Site Is Not, Nor Is It Intended To Be, Legal Advice. You Should Consult An Attorney For Advice Regarding Your Individual Situation.</p>

</body>
</html>
```